BrivoMatex. Lantern for the Steady Growth. Business card

Professional business card for BrivoMatex (Lantern for the Steady Growth)
My rationale: Strategy-> Execution-> Results-> Value that lead to the BrivoMatex name: We put the Lantern for the Steady Growth.
We deliver value to our customers helping them at defining a good strategy (cyan arrow). 90% of well formulated strategies fail due to poor execution so we also consider strategical execution very important (green arrow). Due to the execution we obtain the results (blue arrow). Finally, the results provide feedback to redefine strategy, and the new strategy has to be executed and new results obtained providing new feedback and on and on. It's like a wheel that finally, must create corporate value: value for shareholders, staholders, employees, providers...-

Target Market(s)

CEOs and steering comitees , invewrnent funds

Industry/Entity Type

Business Consultant

Contact Information for Business Card

Tommaso Ferlini
CEO & Founder
tommaso.ferlini@brivomatex.example
Mobile: +34 611.205.938
www.brivomatex.example

Colors

Designer to choose colors to be used in the design.

Requirements
Nice to have
• Nice to hace the words: Strategy, execution, results
• Nice to vave the claim: Lantern for the Steady Growth
• The three colors should be shown:
• cyan for STRATEGY
• green for EXECUTION
• blue for RESULTS
Should not have
• Complete black background

```html
<!DOCTYPE html>
<html lang="en">
<head>
<meta charset="utf-8">
<title>BrivoMatex — Business Card</title>
<link href="https://fonts.googleapis.com/css2?family=Arimo:wght@400;700&display=swap" rel="stylesheet">
<style>
  :root {
    --royal-blue: #0b2f9c;
    --navy-text: #12329a;
    --execution-green: #8cc63f;
    --strategy-cyan: #22aee6;
    --results-blue: #0b2f9c;
    --paper: #ffffff;
    --ink-grey: #4a4a4a;
    --backdrop: #e9ebef;
  }
  * { box-sizing: border-box; margin: 0; padding: 0; }
  html, body {
    width: 1200px; height: 1015px; overflow: hidden;
    background: var(--backdrop);
    font-family: "Arimo", Arial, sans-serif;
  }
  .sheet {
    width: 1200px; height: 1015px;
    display: flex; flex-direction: column; align-items: center; justify-content: center;
    gap: 56px;
  }
  .card {
    position: relative;
    width: 700px; height: 400px;
    overflow: hidden;
    box-shadow: 0 10px 28px rgba(0,0,0,0.18);
  }

  /* Front */
  .card-front {
    background: var(--royal-blue);
    display: flex; flex-direction: column; align-items: center; justify-content: center;
  }
  .front-brand {
    display: flex; align-items: center; gap: 16px;
  }
  .brand-dot {
    width: 26px; height: 26px; border-radius: 50%;
    background: var(--execution-green);
  }
  .front-name {
    font-weight: 700; font-size: 78px; letter-spacing: -1px;
    color: var(--paper);
    line-height: 1;
  }
  .front-claim {
    margin-top: 14px;
    font-weight: 700; font-size: 19px; letter-spacing: 0.5px;
    color: var(--execution-green);
    text-transform: uppercase;
  }

  /* Back */
  .card-back { background: var(--paper); }
  .holder {
    position: absolute; left: 48px; top: 120px;
  }
  .holder-name {
    font-size: 27px; color: var(--navy-text); line-height: 1.1;
  }
  .holder-role {
    font-size: 18px; color: var(--ink-grey); margin-top: 3px;
  }
  .back-brand {
    position: absolute; right: 46px; top: 96px;
    text-align: left;
  }
  .back-name-row { display: flex; align-items: center; gap: 12px; }
  .back-name {
    font-weight: 700; font-size: 58px; letter-spacing: -1px;
    color: var(--navy-text); line-height: 1;
  }
  .back-tagline {
    margin-top: 8px;
    font-size: 21px; color: var(--strategy-cyan);
  }
  .contacts {
    position: absolute; left: 150px; top: 250px;
    list-style: none;
  }
  .contacts li {
    display: flex; align-items: center; gap: 10px;
    font-size: 19px; color: var(--ink-grey); line-height: 25px;
  }
  .contacts svg { width: 18px; height: 18px; flex: none; }
  .band { position: absolute; bottom: 0; }
  .band-strategy  { left: 0;     width: 250px; height: 14px; background: var(--strategy-cyan); }
  .band-execution { left: 258px; width: 230px; height: 34px; background: var(--execution-green); }
  .band-results   { left: 496px; width: 204px; height: 54px; background: var(--results-blue); }
</style>
</head>
<body>
<main class="sheet">

  <section class="card card-front" aria-label="Business card front">
    <div class="front-brand">
      <span class="brand-dot"></span>
      <h1 class="front-name">BrivoMatex</h1>
    </div>
    <p class="front-claim">Lantern for the Steady Growth</p>
  </section>

  <section class="card card-back" aria-label="Business card back">
    <div class="holder">
      <p class="holder-name">Tommaso Ferlini</p>
      <p class="holder-role">CEO &amp; Founder</p>
    </div>

    <div class="back-brand">
      <div class="back-name-row">
        <span class="back-name">BrivoMatex</span>
      </div>
      <p class="back-tagline">Strategy, Execution, Results</p>
    </div>

    <ul class="contacts">
      <li>
        <svg viewBox="0 0 20 20" aria-hidden="true"><path fill="#0b2f9c" d="M5 2l3 3-2 3c1 2 3 4 5 5l2-2 3 3-2 3C8 17 3 12 2 5z"/></svg>
        +34 611.205.938
      </li>
      <li>
        <svg viewBox="0 0 20 20" aria-hidden="true"><rect x="1" y="4" width="18" height="12" fill="#0b2f9c"/><path d="M1 4l9 7 9-7" fill="none" stroke="#fff" stroke-width="1.6"/></svg>
        tommaso.ferlini@brivomatex.example
      </li>
      <li>
        <svg viewBox="0 0 20 20" aria-hidden="true"><circle cx="10" cy="10" r="9" fill="#0b2f9c"/><ellipse cx="10" cy="10" rx="4" ry="9" fill="none" stroke="#fff" stroke-width="1.3"/><path d="M1 10h18" stroke="#fff" stroke-width="1.3"/></svg>
        www.brivomatex.example
      </li>
    </ul>

    <div class="band band-strategy"></div>
    <div class="band band-execution"></div>
    <div class="band band-results"></div>
  </section>

</main>
</body>
</html>
```